Colourful Bold Design for Pet Insurance Website

PLEASE NOTE THAT THIS PROJECT HAS BEEN EXTENDED. Please read the PROJECT EXTENSION DOCUMENT BEFORE STARTING WORK ON ANY DESIGNS.

We are looking for a colourful bold new template design for our JOOMLA HOMEPAGE and a matching design for our new WORDPRESS BLOG.

The website will help pet owners work out which insurance policy best meets their needs. The aim of the website is to explain policy differences in a plain clear manner.

The website will need to have a professional colourful image. It needs to be BOLD, CLEAN AND SHARP rather than soft, pastel and cuddly.

COLOUR SCHEME
The website needs to have a bold colourful design on a white background.
On the inner pages we will have five different types of policies which will be colour coded. We would ideally therefore like to incorporate five distinct colours in the design. See attached document for example of colour schemes we like.

LOGO
We want to keep the existing logo. Please find the file attached. You may though change the logo colours.

CONTENT
One of the reasons for the new design is that we want to change the style of the homepage and include new content. Our current homepage can be found at www.furrow-cover-polls.co.uk.

Content Required
Slideshow
Article Intro.. About Pet Insurance
Policy Lookup Box (see existing site… you can change the design of this)
Six link options (see links on left of current page)
Latest Reviews (List of 6)
Ad (Same dimensions as currently on homepage)

News and Comment Section - To include Three or Four Articles, Title, Intro to article (probably 3 or 4 lines .. about 400px wide), Read more link
Social Media Section
Friendwall Plugin with Feed
Latest Tweets Plugin
Pet Charities Latest Tweets
Footer
Larger footer with lots of links grouped in sections

It does not need to include the clipart pic of the pets which is on the current homepage.

Examples of Websites and Templates We Like
http://www.pawlane.com/ (like colours… fonts…layout)
http://sitetheme.brightkiln.com/?template=upbeat&path=/... (like the clarity, "white" space etc)
http://www.layoutforge.com/demo/51872.html (like white space, clear easy to read fonts… don’t like colour scheme, size of top picture)
http://www.layoutforge.com/website-templates/63915.html (like colour scheme, use of white space)

FEEDBACK
I will provide lots of feedback on all designs submitted so that together we can get the best result.

For clarification this is a DESIGN ONLY project. Our website developer will view the designs before we make our final choice as he wants to ensure he can develop "sharp, practical and most importantly light weight web interface" from the design.

Just updated this brief to clarify design issues, content issues and to give some more examples of site designs I like. 

Please note that although we wish to keep the logo you can change the colours to suit your design. 

Please note that we have now added details of pictures we would be happy to use on the website.  We would prefer it if you used one of these.   Otherwise please ensure your picture includes a nice dog and nice cat and no people!

I have been delighted with the quality of the designs submitted for this project.  So much so that I am going to extend the project to include some additional inner pages.   The amended brief will be posted on here on Friday 10 May.   The deadline will be extended and the budget will also be increased. 

Reason: Additional inner pages now required. Budget will be increased. Revised brief to be posted on here Friday 10 May.

Target Market(s)

Pet owners in the UK who are confused about pet insurance. It therefore needs to be a bold design which is plain, clean and easy to read. It should use bold colours rather than pastels and should not use "cuddly" images.

Industry/Entity Type

Insurance

Requirements
Must have
• Bold clear and distinct colours (preferably 5)
Content as per uploaded file (not just content from existing site)
Easy to read fonts
Should not have
• Pastel colours
Cuddly images

```html
<!DOCTYPE html>
<html lang="en">
<head>
<meta charset="utf-8">
<title>Furrow Cover Polls UK</title>
<link href="https://fonts.googleapis.com/css2?family=Open+Sans:wght@400;600;700;800&family=Oswald:wght@700&display=swap" rel="stylesheet">
<style>
:root{
  --ink:#333;
  --muted:#555;
  --blue:#1f86d4;
  --blue-dark:#1766ad;
  --orange:#f6861f;
  --purple:#9a4fd3;
  --green:#3aa66a;
  --grey:#7a7a7a;
  --head:#3f3f3f;
  --page:#e9e9e9;
  --panel:#f3f3f3;
  --line:#d6d6d6;
  --tick:#1f8a1f;
  --cross:#c62222;
  --footer:#4a4a4a;
  --footer-base:#2c2c2c;
  --ad-green:#2d9a3a;
}
*{box-sizing:border-box;margin:0;padding:0}
html,body{width:1200px;height:2597px;overflow:hidden}
body{background:var(--page);font-family:"Open Sans",Arial,sans-serif;color:var(--ink);position:relative}
.abs{position:absolute}

/* header */
.topbar{left:0;top:0;width:1200px;height:97px;background:#000}
.brand{left:160px;top:18px;display:flex;align-items:center;gap:12px}
.brand-mark{width:46px;height:46px;border-radius:50%;background:var(--blue)}
.brand-name{color:#fff;font-weight:700;font-size:27px;line-height:28px;width:240px}
.search{left:831px;top:33px;width:219px;height:33px;background:#fff;border-radius:3px}
.search svg{position:absolute;right:6px;top:4px}

.nav{left:111px;top:97px;width:980px;height:45px;background:linear-gradient(#3a97e6,#1f74c4);display:flex;align-items:center;justify-content:space-around;padding:0 8px}
.nav a{color:#fff;font-weight:600;font-size:14.5px;text-decoration:none}
.nav-fold-l,.nav-fold-r{top:97px;width:0;height:0;border-top:12px solid #0f4e8c}
.nav-fold-l{left:118px;border-left:0 solid transparent;border-right:0}

.panel{left:118px;top:142px;width:966px;height:2102px;background:#fff}

h1.page-title{left:138px;top:170px;font-size:29px;font-weight:700;color:var(--blue)}

/* policy table */
.policy-table{left:140px;top:215px;width:920px;border:2px solid #cfcfcf;border-radius:3px;background:#fff}
.policy-table .row{display:grid;grid-template-columns:102px 80px 78px 106px 88px 74px 73px 68px 97px 73px 77px;height:59px;border-top:1px solid #e2e2e2}
.policy-table .row.head{height:52px;background:var(--head);color:#fff;border:0}
.policy-table .cell{display:flex;align-items:center;justify-content:center;text-align:center;font-size:12.5px;border-left:1px solid #e2e2e2;line-height:15px}
.policy-table .head .cell{font-size:12.5px;border-left:1px solid #5a5a5a}
.policy-table .name{color:#fff;font-weight:600;font-size:12.5px;border-left:0}
.p1{background:var(--blue)}.p2{background:var(--orange)}.p3{background:var(--purple)}.p4{background:var(--green)}.p5{background:var(--grey)}

/* info boxes */
.box{border:3px solid #e4e4e4;border-radius:4px;background:var(--panel)}
.ratings{left:132px;top:578px;width:289px;height:160px;padding:12px 14px}
.box-title{font-weight:700;font-size:18px;color:var(--blue)}
.rate-row{display:flex;align-items:center;height:28px;font-size:13px;margin-top:2px}
.rate-row .label{width:128px;display:flex;align-items:center;gap:8px}
.bullet{width:13px;height:13px;border-radius:50%;background:var(--orange);display:inline-block;flex:none}
.stars{display:flex;gap:3px}
.band{color:var(--blue-dark);font-weight:600}
.terms{left:445px;top:578px;width:379px;height:160px;background:var(--orange);border-radius:4px;padding:10px 16px;color:#fff}
.terms h2{font-size:18px;font-weight:700}
.terms p{font-size:12px;line-height:17px;color:#4a1d00}
.insurer{left:847px;top:578px;width:223px;height:160px;padding:12px 16px}
.insurer .line{font-size:13px;margin-top:13px}
.insurer .line b{font-weight:400;display:inline-block;width:70px}
.orange-link{color:var(--orange)}
.blue-link{color:var(--blue)}

/* tabs */
.tab-key{left:130px;top:757px;width:156px;height:34px;background:#f2f2f2;border:2px solid #e0e0e0;border-bottom:0;font-weight:600;font-size:18px;display:flex;align-items:center;justify-content:center}
.tab-excess{left:294px;top:757px;width:231px;height:32px;background:var(--blue);color:#fff;font-size:16px;font-weight:600;display:flex;align-items:center;justify-content:center;border-radius:3px 3px 0 0}
.keypoints{left:130px;top:789px;width:622px;height:219px;padding:10px 28px}
.keypoints p{font-size:12px;line-height:19.6px}

.ad-side{left:771px;top:757px;width:299px;height:251px;border:4px solid var(--ad-green);background:#fff}
.ad-side .shop{height:52px;display:flex;align-items:center;gap:8px;padding:0 10px;font-weight:700;font-size:18px;color:#222;border-bottom:1px solid #ddd}
.ad-side .shop i{width:22px;height:22px;background:var(--ad-green)}
.ad-side .art{position:absolute;left:0;top:52px;width:291px;height:191px;background:linear-gradient(#fff,#e8e8e8)}
.ad-side .prod{position:absolute;left:12px;top:62px;font-size:20px;font-weight:600;color:#111}
.ad-side .sub{position:absolute;left:12px;top:88px;font-size:13px;color:#111}
.ad-side .drive{position:absolute;left:160px;top:100px;width:110px;height:110px;background:#222;border-radius:6px}
.ad-side .price{position:absolute;left:16px;top:150px;width:100px;height:40px;background:var(--orange);color:#222;font-weight:800;font-size:18px;display:flex;align-items:center;justify-content:center}
.ad-side .buy{position:absolute;right:0;bottom:0;width:108px;height:30px;background:#c61c1c;color:#fff;font-weight:700;font-size:16px;display:flex;align-items:center;justify-content:center}
.ad-side .perks{position:absolute;left:12px;bottom:6px;font-size:8px;font-weight:700;color:#222}

/* benefits */
.benefits{left:140px;top:1035px;width:610px;height:1081px;border:3px solid #e2e2e2;border-radius:4px;background:var(--panel)}
.bgrid{display:grid;grid-template-columns:333px 141px 130px}
.bhead{height:51px;background:var(--head);color:#fff;font-weight:600;font-size:14px}
.bhead div{display:flex;align-items:center;padding-left:16px;border-right:1px solid #5a5a5a}
.bhead div+div{justify-content:center;padding:0}
.bsec{height:33px;background:#eaeaea;display:flex;align-items:center;padding-left:16px;color:var(--blue);font-weight:600;font-size:14px;border-top:1px solid #fff}
.brow{height:23px;font-size:11.5px;color:#444;background:#fff}
.brow > div{display:flex;align-items:center;border-right:1px solid #e3e3e3}
.brow > div:first-child{padding-left:16px;gap:9px}
.brow > div+div{justify-content:center}
.brow.plain > div:first-child{padding-left:16px}
.note{font-style:italic;font-size:10.5px;color:#666}
.nk{color:var(--blue-dark);font-weight:600;font-size:11.5px}
.amount{color:var(--blue-dark);font-size:11.5px}
.pad{height:8px;background:#fff}
.pad > div{border-right:1px solid #e3e3e3}
.older{padding:10px 16px;font-size:12px;line-height:19px;color:#555}

/* banner */
.banner{left:237px;top:2137px;width:728px;height:90px;background:var(--ad-green);display:flex;align-items:center;padding:0 10px;gap:18px}
.banner .slogan{font-family:"Oswald",Impact,sans-serif;color:#fff;font-size:40px;letter-spacing:.5px}
.banner .ball{width:66px;height:66px;border-radius:50%;background:radial-gradient(#eee,#8a8a8a)}
.banner .org{color:#fff;font-weight:700;font-size:14px;line-height:16px}
.banner .org small{display:block;font-size:9px;font-weight:400}

/* footer */
.footer{left:0;top:2244px;width:1200px;height:298px;background:var(--footer)}
.fbox{top:2273px;height:250px;background:#fff;border-radius:3px}
.fbox .fhead{height:30px;display:flex;align-items:center;gap:8px;padding-left:12px;font-weight:700;font-size:13px;color:#1d4f85}
.fb{left:130px;width:300px}
.fb .fhead{background:#e6eef8}
.fb .fhead i,.tw .fhead i{width:12px;height:12px;background:var(--blue-dark)}
.feed-item{display:flex;gap:8px;padding:8px 12px 0}
.avatar{width:44px;height:44px;flex:none;background:linear-gradient(#e6c9a8,#b98a62)}
.feed-item h4{font-size:12.5px;color:var(--blue-dark);font-weight:600}
.feed-item p{font-size:11px;line-height:15px;color:#444}
.fans{padding:6px 12px 0;font-size:9.5px;color:#333}
.fans b{color:var(--blue-dark)}
.faces{display:flex;gap:4px;padding:6px 12px}
.faces span{width:36px;height:36px;background:linear-gradient(#c9c9c9,#8d8d8d)}
.plugin{padding:4px 12px;font-size:8px;color:#666}
.tw{left:450px;width:302px}
.tw .fhead{background:#5ec9e6;color:#154b6e}
.tweet{padding:12px 18px 10px;border-bottom:1px solid #ddd;margin:0 0 0}
.tweet p{font-size:11px;line-height:16px;color:#444}
.tweet a{color:var(--blue-dark)}
.tweet .meta{font-size:10px;font-style:italic;color:#3a6aa0;margin-top:8px}
.readall{padding:14px 18px;font-weight:700;font-size:12px;color:#333}
.connect{left:824px;top:2275px;color:#fff}
.connect h3{font-size:13px;font-weight:700}
.connect .net{display:flex;align-items:center;gap:14px;margin-top:17px;font-size:12px;color:#ddd}
.connect .net i{width:26px;height:26px;border-radius:3px}
.bottom{left:0;top:2542px;width:1200px;height:55px;background:var(--footer-base);color:#bbb;font-size:11px;display:flex;align-items:center;justify-content:center}
.bottom b{color:#fff;font-weight:400}
</style>
</head>
<body>

<svg width="0" height="0" style="position:absolute">
  <defs>
    <symbol id="tick" viewBox="0 0 24 24"><path d="M3 13l5 6L21 3" fill="none" stroke="#1f8a1f" stroke-width="3.5" stroke-linecap="round" stroke-linejoin="round"/></symbol>
    <symbol id="cross" viewBox="0 0 24 24"><path d="M5 5l14 14M19 5L5 19" stroke="#c62222" stroke-width="4.5" stroke-linecap="round"/></symbol>
    <symbol id="star" viewBox="0 0 24 24"><path d="M12 2l3 7h7l-5.6 4.5 2.1 7.5L12 16.8 5.5 21l2.1-7.5L2 9h7z" fill="#f7c21b"/></symbol>
  </defs>
</svg>

<header class="topbar abs"></header>
<div class="brand abs"><span class="brand-mark"></span><span class="brand-name">Furrow Cover Polls UK</span></div>
<div class="search abs"><svg width="34" height="26" viewBox="0 0 34 26"><circle cx="13" cy="11" r="8" fill="none" stroke="#1f74c4" stroke-width="3"/><path d="M19 17l9 7" stroke="#1f74c4" stroke-width="4" stroke-linecap="round"/></svg></div>

<nav class="nav abs">
  <a href="#">Home</a><a href="#">Policies »</a><a href="#">Glossary</a><a href="#">Fact Sheets</a><a href="#">Survey Reports</a><a href="#">News &amp; Comment</a><a href="#">Contact Us</a>
</nav>

<main class="panel abs"></main>
<h1 class="page-title abs">Furrow Cover Polls UK</h1>

<section class="policy-table abs">
  <div class="row head">
    <div class="cell" style="border-left:0">Policy</div><div class="cell">Vet Fees Limit</div><div class="cell">Excess Range</div><div class="cell">Contribution Range</div><div class="cell">Maximum Age</div><div class="cell">Waiting Period</div><div class="cell">Vet Helpline</div><div class="cell">Pay Vet Direct</div><div class="cell">Price Comparison Sites</div><div class="cell">Online Discount</div><div class="cell">Multipet Discount</div>
  </div>
  <div class="row"><div class="cell name p1">Policy Name</div><div class="cell">£5,000</div><div class="cell">£80-£105</div><div class="cell">0%-20%</div><div class="cell">9 yrs</div><div class="cell">14 Days</div><div class="cell"><svg width="26" height="26"><use href="#tick"/></svg></div><div class="cell"><svg width="18" height="18"><use href="#cross"/></svg></div><div class="cell"><svg width="26" height="26"><use href="#tick"/></svg></div><div class="cell">10%</div><div class="cell">5%</div></div>
  <div class="row"><div class="cell name p2">Policy Name</div><div class="cell">£5,000</div><div class="cell">£80-£105</div><div class="cell">0%-20%</div><div class="cell">9 yrs</div><div class="cell">14 Days</div><div class="cell"><svg width="26" height="26"><use href="#tick"/></svg></div><div class="cell"><svg width="18" height="18"><use href="#cross"/></svg></div><div class="cell"><svg width="26" height="26"><use href="#tick"/></svg></div><div class="cell">10%</div><div class="cell">5%</div></div>
  <div class="row"><div class="cell name p3">Policy Name</div><div class="cell">£5,000</div><div class="cell">£80-£105</div><div class="cell">0%-20%</div><div class="cell">9 yrs</div><div class="cell">14 Days</div><div class="cell"><svg width="26" height="26"><use href="#tick"/></svg></div><div class="cell"><svg width="18" height="18"><use href="#cross"/></svg></div><div class="cell"><svg width="26" height="26"><use href="#tick"/></svg></div><div class="cell">10%</div><div class="cell">5%</div></div>
  <div class="row"><div class="cell name p4">Policy Name</div><div class="cell">£5,000</div><div class="cell">£80-£105</div><div class="cell">0%-20%</div><div class="cell">9 yrs</div><div class="cell">14 Days</div><div class="cell"><svg width="26" height="26"><use href="#tick"/></svg></div><div class="cell"><svg width="18" height="18"><use href="#cross"/></svg></div><div class="cell"><svg width="26" height="26"><use href="#tick"/></svg></div><div class="cell">10%</div><div class="cell">5%</div></div>
  <div class="row"><div class="cell name p5">Policy Name</div><div class="cell">£5,000</div><div class="cell">£80-£105</div><div class="cell">0%-20%</div><div class="cell">9 yrs</div><div class="cell">14 Days</div><div class="cell"><svg width="26" height="26"><use href="#tick"/></svg></div><div class="cell"><svg width="18" height="18"><use href="#cross"/></svg></div><div class="cell"><svg width="26" height="26"><use href="#tick"/></svg></div><div class="cell">10%</div><div class="cell">5%</div></div>
</section>

<section class="ratings box abs">
  <h2 class="box-title">RATINGS</h2>
  <div class="rate-row" style="margin-top:10px"><span class="label"><i class="bullet"></i>Ratewise Rating</span><span class="stars"><svg width="18" height="18"><use href="#star"/></svg><svg width="18" height="18"><use href="#star"/></svg><svg width="18" height="18"><use href="#star"/></svg><svg width="18" height="18"><use href="#star"/></svg><svg width="18" height="18"><use href="#star"/></svg></span></div>
  <div class="rate-row"><span class="label"><i class="bullet"></i>Claims Rating</span><span class="stars"><svg width="18" height="18"><use href="#star"/></svg><svg width="18" height="18"><use href="#star"/></svg><svg width="18" height="18"><use href="#star"/></svg><svg width="18" height="18"><use href="#star"/></svg><svg width="18" height="18"><use href="#star"/></svg></span></div>
  <div class="rate-row"><span class="label"><i class="bullet"></i>Price Band</span><span class="band">£5</span></div>
</section>

<section class="terms abs">
  <h2>TERMS</h2>
  <p>Whilst we have taken great care in ensuring the information below is accurate, we cannot be responsible for its accuracy and you must check all the details with the insurer before purchasing the policy. The details below relate to the current policy available from the insurer. Terms for existing policies you have may be different.</p>
</section>

<section class="insurer box abs">
  <h2 class="box-title">INSURER DETAILS</h2>
  <div class="line"><b>Website:</b><span class="orange-link">Visit Wedsite</span></div>
  <div class="line"><b>Phone:</b><span class="blue-link">0800 415 6620</span></div>
  <div class="line"><b>Underwriter :</b></div>
</section>

<div class="tab-key abs">Key Points</div>
<div class="tab-excess abs">Excess &amp; Contribution</div>
<section class="keypoints box abs">
  <p>Fixed excess is £100.</p>
  <p>Only covers vet treatment for accidents and third party public liability</p>
  <p>Fixed excess is £100.</p>
  <p>20% contribution for pets over 6</p>
  <p>Maximum benefit of £250 per year for treatment of cruciate ligament injuries</p>
  <p>Maximum benefit of £500 per year for CT/MRI scans</p>
  <p>Will not pay for conditions caused by your pet being overweight</p>
  <p>Will only pay for out of hours consultations where your pet was suffering from a life-endangering condition or your vet can confirm in writing that it was essential and not to have done so would have seriously worsened your pets condition.</p>
</section>

<aside class="ad-side abs">
  <div class="shop"><i></i>Shopnest.com</div>
  <div class="art" role="img" aria-label="Product photo of a black USB pen drive with a price tag"></div>
  <div class="prod">Kestrel SwiftDrive</div>
  <div class="sub">4GB Pen Drive</div>
  <div class="drive" role="img" aria-label="Pen drive product shot"></div>
  <div class="price">Rs.299</div>
  <div class="perks">FREE SHIPPING · CASH ON DELIVERY</div>
  <div class="buy">Buy Now</div>
</aside>

<section class="benefits abs">
  <div class="bgrid bhead"><div>Benefits</div><div>Cover Limit</div><div>Cover Limit</div></div>

  <div class="bsec">Complementary Treatments</div>
  <div class="bgrid brow plain"><div class="note">Maximum £250 per annum (included within vet fees benefit)</div><div></div><div></div></div>
  <div class="bgrid brow plain"><div>Herbal medicine</div><div><svg width="20" height="20"><use href="#tick"/></svg></div><div></div></div>
  <div class="bgrid brow plain"><div>Homeopathy</div><div class="nk">N/K</div><div></div></div>
  <div class="bgrid brow plain"><div>Physiotherapy</div><div class="nk">N/K</div><div></div></div>
  <div class="bgrid brow plain"><div>Osteotherapy</div><div><svg width="11" height="11"><use href="#cross"/></svg></div><div></div></div>
  <div class="bgrid brow plain"><div>Chiropractic Treatment</div><div><svg width="11" height="11"><use href="#cross"/></svg></div><div></div></div>
  <div class="bgrid brow plain"><div>Acupuncture Treatment</div><div><svg width="20" height="20"><use href="#tick"/></svg></div><div></div></div>
  <div class="bgrid brow plain"><div>Hydrotherapy</div><div class="nk">N/K</div><div></div></div>
  <div class="bgrid pad"><div></div><div></div><div></div></div>

  <div class="bsec">Additional Benefits</div>
  <div class="bgrid pad"><div></div><div></div><div></div></div>
  <div class="bgrid brow"><div><i class="bullet"></i>Third Party Public Liability</div><div><svg width="20" height="20"><use href="#tick"/></svg></div><div class="amount">£ 1,000,000</div></div>
  <div class="bgrid pad"><div></div><div></div><div></div></div>

  <div class="bsec">Death/Loss Benefits</div>
  <div class="bgrid pad"><div></div><div></div><div></div></div>
  <div class="bgrid brow"><div><i class="bullet"></i>Accidental Death</div><div><svg width="11" height="11"><use href="#cross"/></svg></div><div></div></div>
  <div class="bgrid brow"><div><i class="bullet"></i>Death by Illness</div><div><svg width="11" height="11"><use href="#cross"/></svg></div><div></div></div>
  <div class="bgrid brow"><div><i class="bullet"></i>Lost Or Stolen</div><div><svg width="11" height="11"><use href="#cross"/></svg></div><div></div></div>
  <div class="bgrid pad"><div></div><div></div><div></div></div>

  <div class="bsec">Emergency Pet Care (Boarding)</div>
  <div class="bgrid pad"><div></div><div></div><div></div></div>
  <div class="bgrid brow"><div><i class="bullet"></i>Boarding Kennels</div><div><svg width="11" height="11"><use href="#cross"/></svg></div><div></div></div>
  <div class="bgrid brow"><div><i class="bullet"></i>Daily Minding</div><div><svg width="11" height="11"><use href="#cross"/></svg></div><div></div></div>
  <div class="bgrid pad"><div></div><div></div><div></div></div>

  <div class="bsec">Overseas Travel</div>
  <div class="bgrid pad"><div></div><div></div><div></div></div>
  <div class="bgrid brow"><div><i class="bullet"></i>Vet Treatment Abroad</div><div><svg width="11" height="11"><use href="#cross"/></svg></div><div></div></div>
  <div class="bgrid brow"><div><i class="bullet"></i>Quarantine</div><div><svg width="11" height="11"><use href="#cross"/></svg></div><div></div></div>
  <div class="bgrid brow"><div><i class="bullet"></i>Loss of Documents</div><div><svg width="11" height="11"><use href="#cross"/></svg></div><div></div></div>
  <div class="bgrid brow"><div><i class="bullet"></i>Repeat Tick/Worming</div><div><svg width="11" height="11"><use href="#cross"/></svg></div><div></div></div>
  <div class="bgrid brow"><div><i class="bullet"></i>Emergency Expenses</div><div><svg width="11" height="11"><use href="#cross"/></svg></div><div></div></div>
  <div class="bgrid pad"><div></div><div></div><div></div></div>

  <div class="bsec">Other Benefits</div>
  <div class="bgrid pad"><div></div><div></div><div></div></div>
  <div class="bgrid brow"><div><i class="bullet"></i>Advertising/Reward</div><div><svg width="11" height="11"><use href="#cross"/></svg></div><div></div></div>
  <div class="bgrid brow"><div><i class="bullet"></i>Holidays Cancellation</div><div><svg width="11" height="11"><use href="#cross"/></svg></div><div></div></div>
  <div class="bgrid brow"><div><i class="bullet"></i>Accidental Damage</div><div><svg width="11" height="11"><use href="#cross"/></svg></div><div></div></div>
  <div class="bgrid brow"><div><i class="bullet"></i>Behaviour Consultation</div><div><svg width="11" height="11"><use href="#cross"/></svg></div><div></div></div>
  <div class="bgrid brow"><div><i class="bullet"></i>Referral Travel Cost</div><div class="nk">N/K</div><div></div></div>
  <div class="bgrid pad"><div></div><div></div><div></div></div>

  <div class="bsec">Older Pets</div>
  <p class="older">Aliquam molestie, mi et imperdiet euismod, dui purus auctor tellus, et interdum lacus lectus et ante. Sed accumsan sollicitudin sapien, sit amet adipiscing turpis gravida ac. In congue, neque ac lobortis volutpat, libero mauris varius mi, vitae suscipit ipsum ligula vitae risus. Duis aliquam nibh a dui iaculis viverra id a velit.</p>
</section>

<aside class="banner abs">
  <span class="slogan">AMERICA'S FAVORITE PASTIME</span>
  <span class="ball" role="img" aria-label="Illustration of a baseball wrapped in newsprint"></span>
  <span class="org">Printed Page Project<small>www.printedpageproject.org</small></span>
</aside>

<footer class="footer abs"></footer>

<section class="fbox fb abs">
  <div class="fhead"><i></i>FRIENDWALL FEEDS</div>
  <div class="feed-item"><span class="avatar" role="img" aria-label="Profile photo"></span><div><h4>Lorem ipsum dolor</h4><p>Duis aliquam nibh a dui iaculis viverra id a velit.</p></div></div>
  <div class="feed-item"><span class="avatar" role="img" aria-label="Profile photo"></span><div><h4>Lorem ipsum dolor</h4><p>Duis aliquam nibh a dui iaculis viverra id a velit.</p></div></div>
  <div class="fans">You and 14,596 others like <b>Furrow Cover Polls UK</b></div>
  <div class="faces" role="img" aria-label="Row of follower profile pictures"><span></span><span></span><span></span><span></span><span></span><span></span></div>
  <div class="plugin">Friendwall social plugin</div>
</section>

<section class="fbox tw abs">
  <div class="fhead"><i></i>CHIRPER FEEDS</div>
  <div class="tweet"><p>Vestibulum<a>http://gdjjg@kulkuf</a> aucibus orci luctus et ultrices posuere cubilia....</p><div class="meta">3 hrs ago | Re-Tweet</div></div>
  <div class="tweet"><p>Vestibulum<a>http://gdjjg@kulkuf</a> aucibus orci luctus et ultrices posuere cubilia....</p><div class="meta">3 hrs ago | Re-Tweet</div></div>
  <div class="readall">READ ALL &gt;&gt;</div>
</section>

<section class="connect abs">
  <h3>CONNECT US</h3>
  <div class="net"><i style="background:#3b5b9a"></i>Friendwall</div>
  <div class="net"><i style="background:#3fb4e0"></i>Chirper</div>
  <div class="net"><i style="background:#c4302b"></i>ClipStream</div>
  <div class="net"><i style="background:#f48a1d"></i>Rss Feed</div>
</section>

<div class="bottom abs">Copyright ©2013.&nbsp;<b>Furrow-Cover-Polls UK</b>. All Right Reserved</div>

</body>
</html>
```